Marcelo Vantrini
Tenor & Vocal Coach
mvbaritono@quellmail.net
(713) 562-8307
www.voicefromthecore.net
Want two sided postcard / rack card.4" x 9"
Front - vertical - picture in t-shirt, name, title (Tenor & Vocal Coach), contact information
Back - horizontal - picture in jacket, name, title (Tenor & Vocal Coach), contact information, bio (see attachment for words)
Do not leave space for an address.
Looking for an edgy modern design!

Target Market(s)

Young adults

Requirements
Nice to have
• Will pay extra to get a complimentary business card design, two sided

```html
<!DOCTYPE html>
<html lang="en">
<head>
<meta charset="utf-8">
<title>Marcelo Vantrini – Rack Card</title>
<link href="https://fonts.googleapis.com/css2?family=Parisienne&family=Didact+Gothic&family=Lato:wght@400;700&display=swap" rel="stylesheet">
<style>
  :root{
    --stage:#e9e6e1;
    --charcoal:#3d4045;
    --orange:#ec8232;
    --white:#ffffff;
    --ink:#222326;
    --photo-light:#d9d4c8;
    --photo-mid:#9c9a93;
    --photo-dark:#4f4e4b;
  }
  *{box-sizing:border-box;margin:0;padding:0}
  html,body{width:1200px;height:900px;overflow:hidden}
  body{background:var(--stage);position:relative;font-family:'Lato',sans-serif}

  .card{position:absolute;overflow:hidden;box-shadow:6px 8px 14px rgba(0,0,0,.35)}
  .card svg.shape{position:absolute;inset:0}
  .script-name{font-family:'Parisienne',cursive;color:var(--orange);font-weight:400;white-space:nowrap}
  .title{font-family:'Didact Gothic',sans-serif;font-weight:400;white-space:nowrap}

  /* Front */
  .card-front{left:42px;top:78px;width:375px;height:750px;background:var(--charcoal)}
  .card-front .script-name{position:absolute;left:0;right:0;top:40px;text-align:center;font-size:40px}
  .card-front .title{position:absolute;left:0;right:0;top:96px;text-align:center;font-size:28px;color:var(--white)}
  .front-contact{position:absolute;left:166px;top:664px;color:var(--white)}
  .front-contact .row{display:flex;align-items:center;gap:6px;font-family:'Didact Gothic',sans-serif}
  .front-contact .phone{font-size:19px;font-weight:700;font-family:'Lato',sans-serif}
  .front-contact .email{font-size:15px;margin-top:6px}

  /* Back */
  .card-back{left:437px;top:240px;width:750px;height:372px;background:var(--white)}
  .card-back .script-name{position:absolute;left:55px;top:40px;font-size:40px}
  .card-back .title{position:absolute;left:56px;top:90px;font-size:27px;color:var(--ink)}
  .bio{position:absolute;left:56px;top:142px;width:352px;font-size:11.6px;line-height:1.08;color:var(--ink);text-align:justify}
  .bio p{margin-bottom:6px}
  .back-contact{position:absolute;left:56px;top:300px;color:var(--white)}
  .back-contact .lead{font-family:'Didact Gothic',sans-serif;color:var(--orange);font-size:12px}
  .back-contact .row{display:flex;align-items:center;gap:6px;margin-top:8px;font-size:14.5px;font-weight:700}
  .back-contact .row .sep{width:12px}
</style>
</head>
<body>

<section class="card card-front" aria-label="Rack card front">
  <svg class="shape" width="375" height="750" viewBox="0 0 375 750">
    <defs>
      <linearGradient id="tee-photo" x1="0" y1="0" x2="1" y2="1">
        <stop offset="0" stop-color="#d9d4c8"/>
        <stop offset=".55" stop-color="#9c9a93"/>
        <stop offset="1" stop-color="#4f4e4b"/>
      </linearGradient>
    </defs>
    <path d="M0 178 C90 140 200 128 300 140 C340 145 362 152 375 158 L375 636 C300 640 200 648 120 668 C70 680 30 700 0 706 Z" fill="var(--white)"/>
    <path d="M0 200 C90 160 200 150 300 160 C340 164 362 170 375 176 L375 628 C300 632 200 640 120 660 C70 672 30 690 0 696 Z" fill="var(--orange)"/>
    <path d="M0 212 C90 172 200 162 300 172 C340 176 362 182 375 188 L375 620 C300 624 200 632 120 652 C70 664 30 680 0 686 Z" fill="url(#tee-photo)" role="img" aria-label="Photo of the singer in a grey t-shirt, smiling and leaning against a wall"/>
  </svg>
  <h1 class="script-name">Marcelo Vantrini</h1>
  <p class="title">Tenor &amp; Vocal Coach</p>
  <div class="front-contact">
    <div class="row phone">
      <svg width="14" height="14" viewBox="0 0 14 14" aria-hidden="true"><circle cx="7" cy="7" r="6" fill="none" stroke="var(--orange)" stroke-width="1.4"/><path d="M4.6 4.2 L5.8 4 L6.4 5.6 L5.7 6.1 C6.1 7 6.9 7.8 7.8 8.3 L8.3 7.6 L9.9 8.2 L9.7 9.4 C7 9.6 4.4 7 4.6 4.2Z" fill="var(--orange)"/></svg>
      <span>1 (713) 562-8307</span>
    </div>
    <div class="row email">
      <svg width="12" height="9" viewBox="0 0 12 9" aria-hidden="true"><rect width="12" height="9" fill="var(--orange)"/><path d="M0 0 L6 5 L12 0" fill="none" stroke="var(--white)" stroke-width="1"/></svg>
      <span>mvbaritono@quellmail.net</span>
    </div>
  </div>
</section>

<section class="card card-back" aria-label="Rack card back">
  <svg class="shape" width="750" height="372" viewBox="0 0 750 372">
    <defs>
      <linearGradient id="jacket-photo" x1="0" y1="0" x2="0" y2="1">
        <stop offset="0" stop-color="#c99a82"/>
        <stop offset=".35" stop-color="#3c465a"/>
        <stop offset="1" stop-color="#202633"/>
      </linearGradient>
    </defs>
    <path d="M410 372 L410 20 L730 20 L730 372 Z" fill="url(#jacket-photo)" role="img" aria-label="Portrait of the singer in a dark patterned jacket and open white shirt"/>
    <path d="M0 290 C120 272 260 270 380 290 C480 306 560 318 640 310 C690 305 725 298 750 292 L750 372 L0 372 Z" fill="var(--white)"/>
    <path d="M0 287 C120 268 260 266 380 286 C480 302 560 314 640 306 C690 301 725 292 750 284 L750 296 C725 303 690 310 640 315 C560 323 480 311 380 295 C260 276 120 278 0 296 Z" fill="var(--orange)"/>
    <path d="M0 298 C120 282 260 280 380 300 C480 316 560 328 640 320 C690 315 725 308 750 302 L750 372 L0 372 Z" fill="var(--charcoal)"/>
  </svg>
  <h2 class="script-name">Marcelo Vantrini,</h2>
  <p class="title">Tenor &amp; Vocal Coach</p>
  <div class="bio">
    <p>Marcelo is a local singer and actor who has been working professionally around the country as a concert artist and musical theater performer.</p>
    <p>He studied at the Calloway School of Music, Bayou Crest University and works as a vocal coach with local youths and adults in Houston area.</p>
    <p>Marcelo's goal is to help his students master their individual instrument so that they can achieve a natural and effortless vocal production.</p>
  </div>
  <div class="back-contact">
    <p class="lead">For more information please contact Marcelo today!</p>
    <div class="row">
      <svg width="14" height="14" viewBox="0 0 14 14" aria-hidden="true"><circle cx="7" cy="7" r="6" fill="none" stroke="var(--orange)" stroke-width="1.4"/><path d="M4.6 4.2 L5.8 4 L6.4 5.6 L5.7 6.1 C6.1 7 6.9 7.8 7.8 8.3 L8.3 7.6 L9.9 8.2 L9.7 9.4 C7 9.6 4.4 7 4.6 4.2Z" fill="var(--orange)"/></svg>
      <span>1 (713) 562-8307</span>
      <span class="sep"></span>
      <svg width="13" height="13" viewBox="0 0 14 14" aria-hidden="true"><circle cx="7" cy="7" r="6" fill="var(--orange)"/><ellipse cx="7" cy="7" rx="2.6" ry="6" fill="none" stroke="var(--charcoal)" stroke-width="1"/><path d="M1 7 H13" stroke="var(--charcoal)" stroke-width="1"/></svg>
      <span>www.voicefromthecore.net</span>
    </div>
  </div>
</section>

</body>
</html>
```